Redesign my business cards

I would like pretty much all the same information as my current business cards but redesigned to stand out more and be more unique photo uploaded to show my current business cards don’t mind if you want to remove or replace I for on the back

```html
<!DOCTYPE html>
<html lang="en">
<head>
<meta charset="UTF-8">
<title>Calloway Detailing – Business Card</title>
<link href="https://fonts.googleapis.com/css2?family=Raleway:wght@400;600;700;800;900&display=swap" rel="stylesheet">
<style>
  :root{
    --navy:#17172f;
    --magenta:#a3195b;
    --teal:#2a9db5;
    --white:#ffffff;
    --ink:#1c1c2e;
    --page:#e4e5e8;
  }
  *{margin:0;padding:0;box-sizing:border-box}
  html,body{width:747px;height:1200px;overflow:hidden;background:var(--page);font-family:"Raleway",Arial,sans-serif;color:var(--ink)}
  .sheet{position:relative;width:747px;height:1200px}
  .card{position:absolute;left:63px;width:620px;height:350px;overflow:hidden;box-shadow:0 8px 24px rgba(0,0,0,.18);background:var(--white)}
  .card svg.shapes{position:absolute;inset:0;width:100%;height:100%}
  .card--front{top:170px}
  .card--back{top:650px}

  .brand{position:absolute;left:28px;top:178px;display:flex;align-items:center;gap:10px;color:var(--white);font-weight:800;font-size:15px;letter-spacing:1.5px;text-transform:uppercase;line-height:1.2}
  .brand__dot{width:22px;height:22px;border-radius:50%;background:var(--teal);flex:none}

  .identity{position:absolute;right:32px;top:98px;text-align:right}
  .identity__name{font-weight:900;font-size:34px;letter-spacing:.5px;color:var(--navy);line-height:1}
  .identity__role{font-weight:600;font-size:13px;letter-spacing:3px;color:var(--navy);margin-top:6px}
  .contact{position:absolute;right:32px;top:200px;display:flex;flex-direction:column;gap:12px;align-items:flex-end}
  .contact__row{display:flex;align-items:center;gap:10px;font-weight:700;font-size:15px;color:var(--navy)}
  .contact__icon{width:20px;height:20px;border-radius:50%;background:var(--navy);display:flex;align-items:center;justify-content:center}
  .contact__icon svg{width:11px;height:11px}

  .services{position:absolute;left:30px;right:34px;top:78px;display:flex;flex-direction:column;gap:16px}
  .service__head{display:flex;justify-content:space-between;font-weight:800;font-size:15px;color:var(--navy);letter-spacing:.4px}
  .service__desc{font-size:9.5px;font-weight:400;line-height:1.35;margin-top:4px;max-width:440px;color:var(--ink)}
</style>
</head>
<body>
<main class="sheet">

  <section class="card card--front">
    <svg class="shapes" viewBox="0 0 620 350" preserveAspectRatio="none" aria-hidden="true">
      <rect width="620" height="350" fill="var(--navy)"/>
      <path d="M0 0 H620 V90 L250 135 C160 60 70 30 0 36 Z" fill="var(--magenta)"/>
      <path d="M620 62 C470 70 330 60 270 120 C225 170 235 270 300 350 H620 Z" fill="var(--white)"/>
      <path d="M318 350 C390 318 500 298 620 296 V350 Z" fill="var(--teal)"/>
      <path d="M360 350 C430 330 520 318 620 318 V350 Z" fill="var(--navy)"/>
    </svg>

    <div class="brand"><span class="brand__dot"></span><span>Calloway<br>Detailing</span></div>

    <div class="identity">
      <h1 class="identity__name">REID CALLOWAY</h1>
      <p class="identity__role">OWNER/OPERATOR</p>
    </div>

    <div class="contact">
      <p class="contact__row">0412 555 017
        <span class="contact__icon"><svg viewBox="0 0 24 24"><path fill="#fff" d="M6.6 10.8a15 15 0 0 0 6.6 6.6l2.2-2.2c.3-.3.7-.4 1-.2 1.1.4 2.3.6 3.6.6.6 0 1 .4 1 1V20c0 .6-.4 1-1 1A17 17 0 0 1 3 4c0-.6.4-1 1-1h3.5c.6 0 1 .4 1 1 0 1.3.2 2.5.6 3.6.1.3 0 .7-.2 1z"/></svg></span>
      </p>
      <p class="contact__row">callowaydetailing@mailbox.com
        <span class="contact__icon"><svg viewBox="0 0 24 24"><path fill="#fff" d="M2 5h20v14H2z M3 6l9 7 9-7" stroke="#17172f" stroke-width="1.5"/></svg></span>
      </p>
    </div>
  </section>

  <section class="card card--back">
    <svg class="shapes" viewBox="0 0 620 350" preserveAspectRatio="none" aria-hidden="true">
      <rect width="620" height="350" fill="var(--white)"/>
      <path d="M330 0 C440 24 540 44 620 66 V0 Z" fill="var(--magenta)"/>
      <path d="M420 0 C490 14 560 26 620 40 V0 Z" fill="var(--navy)"/>
      <path d="M0 278 C50 318 140 340 260 350 H0 Z" fill="var(--teal)"/>
      <path d="M0 306 C50 332 120 344 190 350 H0 Z" fill="var(--navy)"/>
    </svg>

    <div class="services">
      <article class="service">
        <div class="service__head"><span>INTERIOR DETAIL</span><span>$150</span></div>
        <p class="service__desc">Vacuum &amp; deep clean of carpets &amp; upholstery or leather treatment, interior trim clean &amp; condition, window polish and treatment, steam clean and stain removal</p>
      </article>
      <article class="service">
        <div class="service__head"><span>EXTERIOR DETAIL</span><span>$250</span></div>
        <p class="service__desc">Exterior wash &amp; polish, exterior trim revive &amp; protector, window polish &amp; treatment, tyre dressing, engine bay cleaned</p>
      </article>
      <article class="service">
        <div class="service__head"><span>FULL EXTREME DETAIL</span><span>$350</span></div>
        <p class="service__desc">Extreme wash &amp; polish, tyre dressing, engine bay cleaned, vacuum &amp; deep clean of carpets &amp; upholstery or leather treatment, interior trim revive &amp; protector, window polish &amp; treatment</p>
      </article>
    </div>
  </section>

</main>
</body>
</html>
```